We need two vector graphics to explain our Ecosystem and Business Model on our website

Dear Designers!
We are launching an influencer management platform tailored for the crypto space. To enhance our website we are looking for 2 vector graphics to show our ecosystem and business model.
Those graphics should fit primary to the current website-draft as well as to our brand identity (brand style guide as attachment)
It should be not too playful but also not too technical/boring. Primary It should be a great modern looking eye-catcher which makes our ecosystem & business idea understandable at the first sight.
At the moment there are two placeholders on our site for which we like the design a lot and we can orientate or adapt those samples. We appreciate creative ideas on adaptions of these sample as well as completely new approaches in regards to the arrangement.
I created a more detailed description here. https://plovenix.net/designs-4RtKqzLm7Vw2X58Hydc3PbY
Please note that those are only sketches to show what we want to display. The arrangement of the data can be totally different and as mentioned above we also appreciate creative approaches :) The most important is that you make sure they fit in the current website template.
We are also looking for a long term partner for upcomming design jobs so If we like your design apporach we would love to work with you long term.
Looking forward to your ideas!
Thank you,
best regards!
Crypto
Crypto Marketing
- Font: Barlow style: normal weight: 100

```html
<!DOCTYPE html>
<html lang="en">
<head>
<meta charset="utf-8">
<title>Vantyx Ecosystem</title>
<link rel="stylesheet" href="https://fonts.googleapis.com/css2?family=Barlow:wght@300;400;600;700&display=swap">
<style>
  :root {
    --bg: #f0f3f7;
    --ink: #3a3f55;
    --ink-dark: #1f2233;
    --label: #50566a;
    --frame: #4d505a;
    --teal: #40e0d8;
    --coin-deep: #2a2470;
    --coin-light: #3aa9c4;
  }
  * { box-sizing: border-box; margin: 0; padding: 0; }
  html, body { width: 853px; height: 1200px; overflow: hidden; background: var(--bg); }
  body { font-family: "Barlow", sans-serif; color: var(--ink); position: relative; }

  .connectors { position: absolute; inset: 0; width: 853px; height: 1200px; }

  .audience {
    position: absolute; left: 285px; width: 280px; height: 84px;
    border: 2px solid var(--frame); border-radius: 24px;
    display: flex; align-items: center; justify-content: center; text-align: center;
    font-weight: 700; font-size: 21px; line-height: 27px; color: var(--ink);
  }
  .audience--brands { top: 132px; }
  .audience--investors { top: 1030px; }

  .product {
    position: absolute; width: 219px;
    border: 1.2px solid var(--frame); background: var(--bg);
    text-align: center;
  }
  .product__icon { position: absolute; }
  .product__title {
    position: absolute; left: 0; right: 0;
    font-weight: 700; font-size: 21px; line-height: 24px; color: var(--ink-dark);
    white-space: nowrap;
  }
  .product__text {
    position: absolute; left: 0; right: 0;
    font-weight: 300; font-size: 16.5px; line-height: 20px; color: var(--ink);
    white-space: nowrap;
  }
  .product--platform { left: 9px; top: 416px; height: 195px; }
  .product--platform .product__title { top: 29px; padding-left: 38px; }
  .product--platform .product__text { top: 61px; }
  .product--platform .product__icon { left: 6px; top: 20px; }

  .product--booster { left: 625px; top: 419px; height: 195px; }
  .product--booster .product__title { top: 28px; padding-left: 46px; }
  .product--booster .product__text { top: 63px; }
  .product--booster .product__icon { left: 21px; top: 11px; }

  .product--vip { left: 317px; top: 821px; height: 157px; }
  .product--vip .product__title { top: 16px; padding-left: 44px; }
  .product--vip .product__text { top: 51px; }
  .product--vip .product__icon { left: 8px; top: 10px; }

  .edge-label {
    position: absolute; font-weight: 300; font-size: 14.5px; line-height: 18.5px; color: var(--label);
  }
  .edge-label--right-aligned { text-align: right; }

  .pressure {
    position: absolute; font-weight: 400; font-size: 14.5px; line-height: 18.5px; color: var(--label);
  }

  .token-name {
    position: absolute; left: 325px; width: 200px; top: 424px; text-align: center;
    font-weight: 700; font-size: 27px; letter-spacing: 0.5px; color: var(--ink);
  }
  .token-art {
    position: absolute; left: 329px; top: 466px; width: 192px; height: 156px;
    border-radius: 18px;
    background: linear-gradient(135deg, var(--coin-light) 0%, var(--coin-deep) 100%);
  }
</style>
</head>
<body>

<svg class="connectors" viewBox="0 0 853 1200" aria-hidden="true">
  <g fill="none" stroke="var(--teal)" stroke-width="1.2">
    <polyline points="315,216 247,285 259,285 259,327 204,327 120,412"/>
    <polyline points="542,216 609,284 583,284 583,331 654,331 735,415"/>
    <polyline points="120,610 198,693 252,693 252,734 231,734 317,820"/>
    <polyline points="741,613 658,698 621,698 621,736 536,820"/>
    <polygon points="251,479 264,479 281,507 264,535 251,535 268,507"/>
    <polygon points="277,479 290,479 307,507 290,535 277,535 294,507"/>
    <polygon points="600,479 587,479 570,507 587,535 600,535 583,507"/>
    <polygon points="574,479 561,479 544,507 561,535 574,535 557,507"/>
    <polygon points="407,640 436,625 464,640 464,657 436,642 407,657"/>
    <polygon points="407,668 436,653 464,668 464,684 436,669 407,684"/>
    <circle cx="425" cy="96" r="8"/>
    <path d="M408 120 a17 13 0 0 1 34 0 Z"/>
    <path d="M414 92 a7 7 0 0 0 -4 12 M436 92 a7 7 0 0 1 4 12"/>
    <path d="M404 117 a10 9 0 0 1 5 -9 M446 117 a10 9 0 0 0 -5 -9"/>
  </g>
  <line x1="426" y1="978" x2="426" y2="1030" stroke="var(--frame)" stroke-width="1"/>
  <g fill="var(--teal)">
    <circle cx="120" cy="412" r="7.5"/>
    <circle cx="735" cy="415" r="7.5"/>
    <circle cx="120" cy="610" r="7.5"/>
    <circle cx="741" cy="613" r="7.5"/>
  </g>
</svg>

<div class="audience audience--brands">For Brands , Influencers<br>&amp; Agencies</div>

<p class="edge-label edge-label--right-aligned" style="left:40px; top:287px; width:211px;">Discover , Manage, Get Found<br>&amp; Increase ROI</p>
<p class="edge-label" style="left:595px; top:288px; width:250px;">Increase Conversion Rate, Volume &amp;<br>Get engagement from real people</p>
<p class="edge-label edge-label--right-aligned" style="left:8px; top:695px; width:238px;">Find new Investment opportunities<br>super early</p>
<p class="edge-label" style="left:625px; top:701px; width:220px;">Engage to earn exclusive<br>whitespots, NFT’s &amp; Airdrops</p>

<section class="product product--platform">
  <svg class="product__icon" width="30" height="30" viewBox="0 0 30 30" aria-hidden="true">
    <rect x="3" y="3" width="24" height="24" rx="3" fill="none" stroke="var(--teal)" stroke-width="1.4"/>
  </svg>
  <h2 class="product__title">Vantyx Platform</h2>
  <p class="product__text">Largest database of<br>verified crypro<br>influencers on Relaygram,<br>Pictoria ,Vidstream ,<br>Clipstar and Chirpline</p>
</section>

<section class="product product--booster">
  <svg class="product__icon" width="36" height="36" viewBox="0 0 36 36" aria-hidden="true">
    <g fill="none" stroke="var(--teal)" stroke-width="1.3" stroke-linejoin="round">
      <path d="M2 34 V22 H8 V34"/>
      <path d="M11 34 V18 H19 V34"/>
      <path d="M22 34 V12 H28 V34"/>
      <path d="M31 34 V4 M28 7 L31 3 L34 7"/>
      <circle cx="15" cy="26" r="3"/>
      <path d="M5 19 V14 M3 16 L5 13 L7 16"/>
    </g>
  </svg>
  <h2 class="product__title">Vantyx Booster</h2>
  <p class="product__text">Highly optimized How to<br>Buy sites with lists on<br>Onboard ,Engage2earn and<br>Analytics function<br>implemented</p>
</section>

<section class="product product--vip">
  <svg class="product__icon" width="44" height="28" viewBox="0 0 44 28" aria-hidden="true">
    <g fill="none" stroke="var(--teal)" stroke-width="1.3" stroke-linejoin="round">
      <path d="M4 10 L10 22 L16 8 L22 20 L28 8 L34 22 L40 10 L37 25 H7 Z"/>
      <circle cx="4" cy="8" r="1.8"/>
      <circle cx="16" cy="5" r="1.8"/>
      <circle cx="28" cy="5" r="1.8"/>
      <circle cx="40" cy="8" r="1.8"/>
      <circle cx="22" cy="3" r="1.8"/>
    </g>
  </svg>
  <h2 class="product__title">Vantyx&nbsp; VIP World</h2>
  <p class="product__text">The exclusive network to<br>discover verified projects<br>before they run their<br>marketing campaigns</p>
</section>

<div class="token-name">VNTX TOKEN</div>
<div class="token-art" role="img" aria-label="Illustration of the VNTX token coin"></div>

<p class="pressure" style="left:251px; top:438px;">Buying<br>Pressure</p>
<p class="pressure" style="left:520px; top:438px; width:80px; text-align:right;">Buying<br>Pressure</p>
<p class="pressure" style="left:393px; top:694px; width:80px; text-align:center;">Buying<br>Pressure</p>

<div class="audience audience--investors">For Investors and<br>Project Scouts</div>

</body>
</html>
```